8 behaviours infographic

We are a portfolio of approx. 200 resources in technology within a financial services enterprise (5000-6000 employees).
Our portfolio name is Harbour and Planner Asset Services.
Our leadership team has collectively defined a set of 8 behaviours that represent how we should behave and interact amongst ourselves.
We need an infographic that can bring these behaviours to life and be displayed around the workplace on large posters where teams work (the words for the behaviours should also be incorporated into the infographic).
We have also included our team's logo, which needs to be incorporated into the infographic.
The 8 behaviours are:
- Listen & show you care
- Support Each Other
- Be Accountable
- Communicate openly
- Collaborate and leverage the collective strength of the group
- Influence the agenda
- Proactive deliberate and team focussed
- Celebrate success & have fun
Look and feel
Each slider illustrates characteristics of the customer's brand and the style your logo design should communicate.

```html
<!DOCTYPE html>
<html lang="en">
<head>
<meta charset="utf-8">
<title>Harbour and Planner Asset Services – The 8 Behaviours</title>
<link href="https://fonts.googleapis.com/css2?family=Roboto+Condensed:wght@300;400&display=swap" rel="stylesheet">
<style>
  :root {
    --ink: #111418;
    --label: #3a3a3a;
    --brand: #0f2a4a;
    --wheel-bg: #f5f5f5;
    --dots: #9a9a9a;
    --on-colour: #ffffff;
  }
  html, body {
    margin: 0;
    padding: 0;
    width: 927px;
    height: 1200px;
    overflow: hidden;
    background: #ffffff;
  }
  .poster {
    position: relative;
    width: 927px;
    height: 1200px;
    font-family: "Roboto Condensed", sans-serif;
    color: var(--ink);
  }
  .poster svg { display: block; }
  .brand-name {
    font-family: "Roboto Condensed", sans-serif;
    font-weight: 400;
    fill: var(--brand);
    font-size: 42px;
    letter-spacing: 0.5px;
  }
  .headline { font-family: "Roboto Condensed", sans-serif; fill: var(--ink); }
  .headline-small { font-size: 24px; font-weight: 400; }
  .headline-eight { font-size: 128px; font-weight: 400; }
  .headline-large { font-size: 54px; font-weight: 400; }
  .behaviour-label {
    font-family: "Roboto Condensed", sans-serif;
    font-weight: 300;
    font-size: 17px;
    text-anchor: middle;
  }
  .behaviour-label--outside { fill: var(--label); }
  .behaviour-label--inside { fill: var(--on-colour); opacity: 0.85; }
  .connector { stroke: var(--dots); stroke-width: 3; stroke-dasharray: 3 4; }
  .icon-slot { fill: rgba(255, 255, 255, 0.28); }
</style>
</head>
<body>
<main class="poster">
<svg width="927" height="1200" viewBox="0 0 927 1200" xmlns="http://www.w3.org/2000/svg">
  <defs>
    <linearGradient id="grad-listen" gradientUnits="userSpaceOnUse" x1="371" y1="0" x2="557" y2="0">
      <stop offset="0" stop-color="#f4ea4e"/><stop offset="1" stop-color="#e2d21b"/>
    </linearGradient>
    <linearGradient id="grad-support" gradientUnits="userSpaceOnUse" x1="318" y1="0" x2="610" y2="0">
      <stop offset="0" stop-color="#f48d50"/><stop offset="1" stop-color="#ef6127"/>
    </linearGradient>
    <linearGradient id="grad-accountable" gradientUnits="userSpaceOnUse" x1="371" y1="0" x2="557" y2="0">
      <stop offset="0" stop-color="#e0505f"/><stop offset="1" stop-color="#ae1f34"/>
    </linearGradient>
    <linearGradient id="grad-communicate" gradientUnits="userSpaceOnUse" x1="318" y1="0" x2="610" y2="0">
      <stop offset="0" stop-color="#d4178b"/><stop offset="1" stop-color="#9c2585"/>
    </linearGradient>
    <linearGradient id="grad-collaborate" gradientUnits="userSpaceOnUse" x1="371" y1="0" x2="557" y2="0">
      <stop offset="0" stop-color="#5e2f90"/><stop offset="1" stop-color="#8c2a88"/>
    </linearGradient>
    <linearGradient id="grad-influence" gradientUnits="userSpaceOnUse" x1="318" y1="0" x2="610" y2="0">
      <stop offset="0" stop-color="#4a3c7e"/><stop offset="1" stop-color="#2357a8"/>
    </linearGradient>
    <linearGradient id="grad-proactive" gradientUnits="userSpaceOnUse" x1="371" y1="0" x2="557" y2="0">
      <stop offset="0" stop-color="#1e6d8b"/><stop offset="1" stop-color="#1faa98"/>
    </linearGradient>
    <linearGradient id="grad-celebrate" gradientUnits="userSpaceOnUse" x1="318" y1="0" x2="610" y2="0">
      <stop offset="0" stop-color="#1da99b"/><stop offset="1" stop-color="#7cc243"/>
    </linearGradient>
    <radialGradient id="grad-hub" cx="0.45" cy="0.4" r="0.7">
      <stop offset="0" stop-color="#ffffff"/><stop offset="1" stop-color="#d9dbe0"/>
    </radialGradient>
    <filter id="hub-shadow" x="-20%" y="-20%" width="140%" height="140%">
      <feDropShadow dx="0" dy="4" stdDeviation="6" flood-color="#000" flood-opacity="0.18"/>
    </filter>
    <path id="segment-small" d="M371,492.3 A272 272 0 0 1 557,492.3 L513.2,612.7 A144 144 0 0 0 414.8,612.7 Z"/>
    <path id="segment-large" d="M317.6,345.8 A428 428 0 0 1 610.4,345.8 L540.6,537.4 A224 224 0 0 0 387.4,537.4 Z"/>
  </defs>

  <!-- Brand header -->
  <g class="brand">
    <text class="brand-name" x="463.5" y="82" text-anchor="middle">Harbour and Planner</text>
    <text class="brand-name" x="463.5" y="138" text-anchor="middle">Asset Services</text>
  </g>

  <!-- Headline -->
  <g class="headline">
    <text class="headline-small" x="248" y="228">THE</text>
    <text class="headline-eight" x="294" y="290">8</text>
    <text class="headline-large" x="369" y="244">BEHAVIOURS</text>
    <text class="headline-large" x="369" y="290">ARE</text>
  </g>

  <!-- Behaviour wheel -->
  <g class="wheel">
    <circle class="wheel-backdrop" cx="464" cy="748" r="412" fill="var(--wheel-bg)"/>

    <g class="connectors">
      <line class="connector" x1="464" y1="630" x2="464" y2="612" transform="rotate(0 464 748)"/>
      <line class="connector" x1="464" y1="630" x2="464" y2="604" transform="rotate(90 464 748)"/>
      <line class="connector" x1="464" y1="630" x2="464" y2="612" transform="rotate(180 464 748)"/>
      <line class="connector" x1="464" y1="630" x2="464" y2="604" transform="rotate(270 464 748)"/>
      <line class="connector" x1="464" y1="630" x2="464" y2="530" transform="rotate(45 464 748)"/>
      <line class="connector" x1="464" y1="630" x2="464" y2="530" transform="rotate(135 464 748)"/>
      <line class="connector" x1="464" y1="630" x2="464" y2="530" transform="rotate(225 464 748)"/>
      <line class="connector" x1="464" y1="630" x2="464" y2="530" transform="rotate(315 464 748)"/>
    </g>

    <g class="segments">
      <use href="#segment-small" fill="url(#grad-listen)" transform="rotate(0 464 748)"/>
      <use href="#segment-large" fill="url(#grad-support)" transform="rotate(45 464 748)"/>
      <use href="#segment-small" fill="url(#grad-accountable)" transform="rotate(90 464 748)"/>
      <use href="#segment-large" fill="url(#grad-communicate)" transform="rotate(135 464 748)"/>
      <use href="#segment-small" fill="url(#grad-collaborate)" transform="rotate(180 464 748)"/>
      <use href="#segment-large" fill="url(#grad-influence)" transform="rotate(225 464 748)"/>
      <use href="#segment-small" fill="url(#grad-proactive)" transform="rotate(270 464 748)"/>
      <use href="#segment-large" fill="url(#grad-celebrate)" transform="rotate(315 464 748)"/>
    </g>

    <g class="icon-slots">
      <circle class="icon-slot" cx="464" cy="530" r="36" role="img" aria-label="Ear icon for listening"/>
      <circle class="icon-slot" cx="676" cy="484" r="40" role="img" aria-label="Icon of people helping each other"/>
      <circle class="icon-slot" cx="672" cy="744" r="36" role="img" aria-label="Clipboard checklist icon"/>
      <circle class="icon-slot" cx="684" cy="940" r="40" role="img" aria-label="Icon of two people in conversation"/>
      <circle class="icon-slot" cx="464" cy="962" r="36" role="img" aria-label="Icon of a group with a speech bubble"/>
      <circle class="icon-slot" cx="232" cy="944" r="40" role="img" aria-label="Icon of a person broadcasting"/>
      <circle class="icon-slot" cx="248" cy="750" r="36" role="img" aria-label="Icon of a person in a target"/>
      <circle class="icon-slot" cx="236" cy="484" r="40" role="img" aria-label="Icon of a person celebrating"/>
    </g>

    <g class="hub">
      <circle cx="464" cy="748" r="116" fill="url(#grad-hub)" filter="url(#hub-shadow)"/>
      <ellipse cx="458" cy="738" rx="86" ry="64" fill="#f1ea3c" role="img" aria-label="Brain illustration"/>
    </g>

    <g class="labels">
      <text class="behaviour-label behaviour-label--outside" x="464" y="419">LISTEN &amp;
        <tspan x="464" dy="22">SHOW  YOU CARE</tspan></text>
      <text class="behaviour-label behaviour-label--inside" x="682" y="561">SUPPORT
        <tspan x="682" dy="22">EACH OTHER</tspan></text>
      <text class="behaviour-label behaviour-label--outside" x="808" y="725">BE
        <tspan x="808" dy="22">ACCOUNTABLE</tspan></text>
      <text class="behaviour-label behaviour-label--inside" x="682" y="1020">COMMUNICATE
        <tspan x="682" dy="22">OPENLY</tspan></text>
      <text class="behaviour-label behaviour-label--outside" x="460" y="1065">COLLABORATE AND
        <tspan x="460" dy="22">LEVERAGE THE COLLECTIVE</tspan>
        <tspan x="460" dy="22">STRENGTH OF THE GROUP</tspan></text>
      <text class="behaviour-label behaviour-label--inside" x="227" y="1023">INFLUENCE
        <tspan x="227" dy="22">THE AGENDA</tspan></text>
      <text class="behaviour-label behaviour-label--outside" x="121" y="721">PROACTIVE
        <tspan x="121" dy="22">DELIBERATE</tspan>
        <tspan x="121" dy="22">AND TEAM</tspan>
        <tspan x="121" dy="22">FOCUSSED</tspan></text>
      <text class="behaviour-label behaviour-label--inside" x="236" y="553">CELEBRATE
        <tspan x="236" dy="22">SUCCESS &amp;</tspan>
        <tspan x="236" dy="22">HAVE FUN</tspan></text>
    </g>
  </g>
</svg>
</main>
</body>
</html>
```